Labeling for Organic Food

we need a label design for

1. Organic Red Rice
2. Organic wild honey

it is going to be the same design in different dimensions.

1. Organic Red Rice
Dimension 1 28*18.5cm
Dimension 2 13.5*8cm

2. Organic Honey
12*6cm
Updates

There is an update in the brief about using the Bhutanese color scheme. Please check it out.

Target Market(s)

people with the concern of health and the environment.

Requirements
Must have
• 1. our logo
• 2. All the info
• 3. A natural feel
• 4. I would prefer minimalistic style
• 5. Please include Bhutanese national colours as attached.

```html
<!DOCTYPE html>
<html lang="en">
<head>
<meta charset="UTF-8">
<title>Organic Wild Honey Label</title>
<link rel="stylesheet" href="https://fonts.googleapis.com/css2?family=Quicksand:wght@500;600;700&family=Nunito:wght@400;800&display=swap">
<style>
  :root {
    --label-yellow: #fdd64b;
    --label-white: #ffffff;
    --ink: #1c1c1c;
    --honey-purple: #4f3b7b;
    --band-purple-deep: #4a2f74;
    --band-purple-light: #8a5aa8;
  }
  * { margin: 0; padding: 0; box-sizing: border-box; }
  html, body {
    width: 1200px;
    height: 601px;
    overflow: hidden;
    background: var(--label-yellow);
  }
  .label {
    position: relative;
    width: 1200px;
    height: 601px;
    background: var(--label-yellow);
    font-family: "Nunito", Arial, sans-serif;
    color: var(--ink);
  }
  .label__panel {
    position: absolute;
    left: 30px;
    top: 14px;
    width: 1140px;
    height: 572px;
    background: var(--label-white);
  }
  .brand {
    position: absolute;
    top: 34px;
    left: 0;
    width: 100%;
    text-align: center;
    font-family: "Quicksand", Arial, sans-serif;
    font-weight: 700;
    font-size: 56px;
    line-height: 1;
    color: var(--ink);
  }
  .product-title {
    position: absolute;
    top: 128px;
    left: 0;
    width: 100%;
    text-align: center;
    font-family: "Quicksand", Arial, sans-serif;
    font-weight: 600;
    font-size: 78px;
    line-height: 1;
    color: var(--honey-purple);
  }
  .description {
    position: absolute;
    top: 222px;
    left: 100px;
    width: 1000px;
    text-align: center;
    font-size: 20.5px;
    line-height: 26px;
  }
  .facts {
    position: absolute;
    top: 348px;
    left: 0;
    width: 100%;
    text-align: center;
    font-size: 20px;
    line-height: 29px;
  }
  .facts strong, .distributor strong { font-weight: 800; }
  .pattern-band {
    position: absolute;
    left: 0;
    top: 407px;
    width: 1200px;
    height: 98px;
    background: linear-gradient(90deg, var(--band-purple-deep), var(--band-purple-light), var(--band-purple-deep), var(--band-purple-light), var(--band-purple-deep));
  }
  .footer-note {
    position: absolute;
    top: 517px;
    font-size: 21px;
    line-height: 29px;
  }
  .footer-note--left { left: 41px; }
  .footer-note--right { right: 47px; text-align: right; }
  .distributor {
    position: absolute;
    top: 517px;
    left: 0;
    width: 100%;
    text-align: center;
    font-size: 21px;
    line-height: 29px;
    font-weight: 800;
  }
</style>
</head>
<body>
  <main class="label">
    <div class="label__panel"></div>

    <div class="brand">Leafmere</div>
    <h1 class="product-title">Organic Wild Honey</h1>

    <p class="description">
      Oragnic Wild Honey is freshly collected from the remote unpolluted lands of the
      Himalayans in Bhutan. The bees are not fed sugar and antibiotics and the honey
      is free from chemical preservatives, coloring, and additives. The wild honey is not heat
      treated and unprocessed to retain the optimum level of nutritional value and enzymes.
    </p>

    <div class="facts">
      <p><strong>Ingredients:</strong> Organic Bhutanese Wild Honey</p>
      <p><strong>Net Weight:</strong> 250ml</p>
    </div>

    <div class="pattern-band" role="img" aria-label="Band of nested purple diamond pattern in Bhutanese style"></div>

    <div class="footer-note footer-note--left">
      <p>Best before 31/12/19</p>
      <p>Product of Bhutan</p>
    </div>

    <div class="distributor">
      <p>Distributed by Leafmere</p>
      <p>42 Kestrel Lane Singapore 600123</p>
    </div>

    <div class="footer-note footer-note--right">
      <p>Store in a cool</p>
      <p>and dry place</p>
    </div>
  </main>
</body>
</html>
```